New IT Consulting Company website - name is Brolund Consulting

Seeking a new IT Consulting company website in Wordpress, some IT recruitment based skills, about us, services, we have all the content and wireframe details. We then want to build it in Divi ideally

Target Market(s)

IT Consulting companies and also staff augmentation needs

Industry/Entity Type

It Professional

Colors
0355a3

Requirements
Must have
• Home Page,
• Banner (Slider) - What we do
• Banner 2 - Companies / Talent we deal with (Pravtek, Denvik, QTR, Korlu, Tessavane etc)
• Our 3 key areas being:
• a) Integration Consulting and Staff Augmentation
• b) Software Development
• c) Data Consulting and Staff Augmentation
• About Data landing page
• About Integration landing page
• Media (news/blog)
• Contact Us
• Then About us - What we Do, How we do it, our values
• Our Solutions Page - Clients landing Page, Candidates landing Page
• Case Studies page
• Blog
• Contact Us
Nice to have
• NA
Should not have
• NA

```html
<!DOCTYPE html>
<html lang="en">
<head>
<meta charset="utf-8">
<title>Case Studies | Brolund Consulting</title>
<link href="https://fonts.googleapis.com/css2?family=Ubuntu:wght@500;700&family=Open+Sans:wght@400;600;700&display=swap" rel="stylesheet">
<style>
:root{
  --blue:#2a7fe9;
  --link:#1f73de;
  --green:#19d38e;
  --page-green:#2fc46f;
  --navy:#232b3d;
  --ink:#1e1e1e;
  --muted:#7a7a7a;
  --white:#ffffff;
}
*{box-sizing:border-box;margin:0;padding:0}
html,body{width:1200px;height:2899px;overflow:hidden}
body{position:relative;background:var(--white);font-family:"Open Sans",sans-serif;color:var(--ink)}
.abs{position:absolute}
.band{position:absolute;left:0;width:1200px}
.brand{font-family:"Ubuntu",sans-serif;font-weight:700;color:var(--white);white-space:nowrap}
.nav a{position:absolute;top:39px;color:var(--white);text-decoration:none;font-size:14.5px;padding-bottom:5px;white-space:nowrap}
.nav a.active{font-weight:700;border-bottom:2px solid var(--white)}
.btn-contact{left:989px;top:25px;width:121px;height:47px;background:var(--green);border-radius:5px;color:var(--white);font-family:"Ubuntu",sans-serif;font-weight:700;font-size:18px;display:flex;align-items:center;justify-content:center;white-space:nowrap}
.page-title{top:118px;left:0;width:1200px;text-align:center;font-family:"Ubuntu",sans-serif;font-weight:700;font-size:56px;color:var(--white)}
.crumbs{top:193px;left:0;width:1200px;text-align:center;color:var(--white);font-size:15px;display:flex;justify-content:center;align-items:center;gap:12px}
.filters{top:396px;left:0;width:1200px;display:flex;justify-content:center;gap:37px;font-size:15px;color:#555}
.filters .on{color:var(--page-green);font-weight:700}
.card{position:absolute;width:475px;height:483px;background:var(--white);box-shadow:0 4px 14px rgba(0,0,0,.12)}
.card .art{width:475px;height:307px}
.card h3{position:absolute;left:28px;top:325px;font-family:"Ubuntu",sans-serif;font-weight:500;font-size:23px;color:var(--ink)}
.card p{position:absolute;left:29px;top:358px;width:425px;font-size:12px;line-height:25px;color:var(--muted)}
.card .more{position:absolute;left:29px;top:445px;font-size:16px;font-weight:700;color:var(--link)}
.pager{top:2120px;left:497px;display:flex;align-items:center;gap:14px;font-size:13px}
.pager .cur{width:36px;height:36px;border-radius:50%;background:var(--page-green);color:var(--white);display:flex;align-items:center;justify-content:center}
.pager .next{width:90px;height:32px;border:1px solid #ddd;border-radius:16px;display:flex;align-items:center;justify-content:center;margin-left:6px}
.cta-title{top:2322px;left:0;width:1200px;text-align:center;font-family:"Ubuntu",sans-serif;font-weight:700;font-size:41px;color:var(--white)}
.cta-bar{top:2381px;left:551px;width:90px;height:6px;border-radius:3px;background:var(--white)}
.cta-text{top:2398px;left:290px;width:620px;text-align:center;font-size:15px;line-height:20px;color:#d4d8e0}
.cta-btn{top:2457px;left:511px;width:178px;height:47px;border-radius:5px;background:var(--green);color:var(--white);font-family:"Ubuntu",sans-serif;font-weight:700;font-size:18px;display:flex;align-items:center;justify-content:center}
.foot-brand{top:2570px;left:89px;font-size:37px}
.foot-about{top:2633px;left:89px;width:345px;font-size:12.5px;line-height:22.5px;color:#dfe2e8}
.social{top:2738px;left:89px;display:flex;gap:11px}
.social span{width:30px;height:30px;border-radius:50%;background:#3a4356}
.col h4{font-family:"Ubuntu",sans-serif;font-weight:700;font-size:21px;color:var(--white);margin-bottom:12px}
.col li{list-style:none;font-size:15px;color:#e5e8ee;line-height:32px;white-space:nowrap}
.contact li{display:flex;gap:8px;align-items:flex-start;line-height:22px;margin-bottom:10px;font-size:14.5px;white-space:normal}
.contact b{font-weight:700}
.contact svg{flex:none;margin-top:2px}
.map{color:var(--green);font-weight:700;text-decoration:underline}
.rule{top:2848px;left:89px;width:1022px;height:1px;background:#3a4356}
.legal{top:2864px;font-size:14.5px;color:#e5e8ee;white-space:nowrap}
</style>
</head>
<body>

<svg class="band" style="top:0" width="1200" height="347" viewBox="0 0 1200 347" aria-hidden="true">
  <polygon points="0,0 1200,0 1200,220 0,347" fill="var(--blue)"/>
</svg>

<div class="abs brand" style="top:26px;left:89px;font-size:28px">Brolund Consulting</div>
<nav class="nav">
  <a style="left:386px">Home</a>
  <a style="left:463px">About Us</a>
  <a style="left:561px">Our Solutions</a>
  <a style="left:689px">Testimonials</a>
  <a class="active" style="left:809px">Case Studies</a>
  <a style="left:935px">Blog</a>
</nav>
<div class="abs btn-contact">Contact Us</div>

<h1 class="abs page-title">Case Studies</h1>
<div class="abs crumbs">
  <span style="display:flex;align-items:center;gap:4px">
    <svg width="18" height="16" viewBox="0 0 18 16"><path d="M9 1 1 8h2v7h4v-5h4v5h4V8h2z" fill="#fff"/></svg>Home
  </span>
  <span>|</span><span>Case studies</span>
</div>

<div class="abs filters">
  <span class="on">All</span><span>Ecommerce</span><span>Featured</span><span>SEO</span><span>Technology</span>
</div>

<article class="card" style="left:90px;top:448px">
  <div class="art" role="img" aria-label="Illustration of a browser window with domain extensions" style="background:linear-gradient(160deg,#0c3a78,#123f7c)"></div>
  <h3>Heading Goes Here</h3>
  <p>Lorem Ipsum is simply dummy text of the printing &amp; typesetting industry. Lorem Ipsum has been the industry's standard dummy text ever since the 1500s, when an unknown printer...</p>
  <div class="more">Learn More &raquo;</div>
</article>

<article class="card" style="left:636px;top:493px">
  <div class="art" role="img" aria-label="Illustration of responsive website on desktop, laptop and phone" style="background:linear-gradient(160deg,#57cbf6,#43bdf0)"></div>
  <h3>Heading Goes Here</h3>
  <p>Lorem Ipsum is simply dummy text of the printing &amp; typesetting industry. Lorem Ipsum has been the industry's standard dummy text ever since the 1500s, when an unknown printer...</p>
  <div class="more">Learn More &raquo;</div>
</article>

<article class="card" style="left:90px;top:985px">
  <div class="art" role="img" aria-label="Isometric illustration of a cloud-connected workspace" style="background:linear-gradient(135deg,#5a2fe0,#a52ad6 60%,#c22fcf)"></div>
  <h3>Heading Goes Here</h3>
  <p>Lorem Ipsum is simply dummy text of the printing &amp; typesetting industry. Lorem Ipsum has been the industry's standard dummy text ever since the 1500s, when an unknown printer...</p>
  <div class="more">Learn More &raquo;</div>
</article>

<article class="card" style="left:636px;top:1030px">
  <div class="art" role="img" aria-label="Isometric illustration of a laptop with analytics charts" style="background:linear-gradient(160deg,#5667bd,#4252a6)"></div>
  <h3>Heading Goes Here</h3>
  <p>Lorem Ipsum is simply dummy text of the printing &amp; typesetting industry. Lorem Ipsum has been the industry's standard dummy text ever since the 1500s, when an unknown printer...</p>
  <div class="more">Learn More &raquo;</div>
</article>

<article class="card" style="left:90px;top:1522px">
  <div class="art" role="img" aria-label="Illustration of search engine optimisation with a search bar" style="background:linear-gradient(180deg,#bff8f2,#aef3ec)"></div>
  <h3>Heading Goes Here</h3>
  <p>Lorem Ipsum is simply dummy text of the printing &amp; typesetting industry. Lorem Ipsum has been the industry's standard dummy text ever since the 1500s, when an unknown printer...</p>
  <div class="more">Learn More &raquo;</div>
</article>

<article class="card" style="left:636px;top:1567px">
  <div class="art" role="img" aria-label="Illustration of an approved mobile payment" style="background:linear-gradient(135deg,#10c39b,#077a7a 50%,#04234f)"></div>
  <h3>Heading Goes Here</h3>
  <p>Lorem Ipsum is simply dummy text of the printing &amp; typesetting industry. Lorem Ipsum has been the industry's standard dummy text ever since the 1500s, when an unknown printer...</p>
  <div class="more">Learn More &raquo;</div>
</article>

<div class="abs pager">
  <span class="cur">1</span><span>2</span><span class="next">Next</span>
</div>

<svg class="band" style="top:2184px" width="1200" height="715" viewBox="0 0 1200 715" aria-hidden="true">
  <polygon points="0,146 1200,0 1200,715 0,715" fill="var(--navy)"/>
</svg>

<h2 class="abs cta-title">Be A Part Of IT Consulting</h2>
<div class="abs cta-bar"></div>
<p class="abs cta-text">It is a long established fact that a reader will be distracted by the readable content of a page when looking at its layout.</p>
<div class="abs cta-btn">Join Us Today</div>

<div class="abs brand foot-brand">Brolund Consulting</div>
<p class="abs foot-about">But I must explain to you how all this mistaken idea of denouncing pleasure and praising pain was born and I will give you a complete account of the system, and expound the actual teachings of the great explorer of the truth</p>
<div class="abs social" aria-label="Social links"><span></span><span></span><span></span><span></span></div>

<div class="abs col" style="top:2568px;left:495px">
  <h4>Quick Links</h4>
  <ul><li>Home</li><li>About Us</li><li>Services</li><li>Portfolio</li><li>Contact</li></ul>
</div>
<div class="abs col" style="top:2568px;left:669px">
  <h4>Services</h4>
  <ul><li>App Development</li><li>Software Support</li><li>Data Management</li><li>Network Security</li><li>Cloud Computing</li></ul>
</div>
<div class="abs col contact" style="top:2568px;left:855px;width:260px">
  <h4 style="margin-left:12px">Contact</h4>
  <ul>
    <li><svg width="18" height="20" viewBox="0 0 18 20"><path d="M9 1a6 6 0 0 0-6 6c0 5 6 11 6 11s6-6 6-11a6 6 0 0 0-6-6z" fill="none" stroke="#fff" stroke-width="1.5"/><circle cx="9" cy="7" r="2" fill="none" stroke="#fff" stroke-width="1.5"/></svg><span><b>location:</b> Level 4, 18 Harbour Lane, Sydney, 2000, NSW (map)</span></li>
    <li><svg width="30" height="16" viewBox="0 0 30 16"><path d="M0 4h8M2 8h6M0 12h8" stroke="#fff" stroke-width="1.3"/><rect x="10" y="1" width="19" height="14" fill="none" stroke="#fff" stroke-width="1.4"/><path d="m10 1 9.5 8L29 1" fill="none" stroke="#fff" stroke-width="1.4"/></svg><span><b>Email:</b> Email Us</span></li>
    <li><svg width="20" height="18" viewBox="0 0 20 18"><path d="M4 1 1 4c0 7 6 13 13 13l3-3-4-3-2 2c-3-1-5-3-6-6l2-2z" fill="none" stroke="#fff" stroke-width="1.4"/></svg><span><b>Phone:</b> 02 5550 1842</span></li>
    <li><svg width="18" height="18" viewBox="0 0 18 18"><circle cx="9" cy="9" r="7.5" fill="none" stroke="#fff" stroke-width="1.3"/><ellipse cx="9" cy="9" rx="3.2" ry="7.5" fill="none" stroke="#fff" stroke-width="1.3"/><path d="M1.5 9h15" stroke="#fff" stroke-width="1.3"/></svg><span><b>Web:</b> www.brolundconsulting.com</span></li>
    <li style="margin-left:37px"><span class="map">View Map</span></li>
  </ul>
</div>

<div class="abs rule"></div>
<div class="abs legal" style="left:89px">&copy; Copyright 2019 &middot; All rights reserved</div>
<div class="abs legal" style="left:888px">Terms &amp; Condition</div>
<div class="abs legal" style="left:1026px">Privacy Policy</div>

</body>
</html>
```